Building Referrer Relationships Booklet

4 page A4 booklet to give to potential professional referrers to establish a collaborative relationship.Needs to be bright, vibrant, colourful, friendly, inviting, in keeping with The Stride Studio colours.
Want to provide potential referrer partners a great reason to choose to collaborate with us. They need to know who we are, what makes us different/appealing, and who we are looking for to connect with.
The final product should communicate high performance and connectedness.

Target Market(s)

professional medical allied health and fitness practitioners

Industry/Entity Type

Health

Requirements
Must have
• energetic, vibrant, engaging, inviting, images

```html
<!DOCTYPE html>
<html lang="en">
<head>
<meta charset="utf-8">
<title>The Stride Studio – Referrer Booklet Spread</title>
<link href="https://fonts.googleapis.com/css2?family=Questrial&family=PT+Serif:ital,wght@0,400;0,700;1,400&display=swap" rel="stylesheet">
<style>
  :root{
    --bg:#e4e5e7;
    --paper:#f4f4f5;
    --ink:#2b2b2b;
    --orange:#ee9a2b;
    --deep-orange:#e8621c;
    --red:#d9262d;
    --amber:#f0a21e;
    --green:#3da83a;
    --dark-green:#2d7a2f;
    --teal:#3fb6a6;
    --blue:#1e6fc0;
    --sky:#2a9fe0;
    --slate:#58585a;
  }
  *{box-sizing:border-box;margin:0;padding:0}
  html,body{width:1200px;height:840px;overflow:hidden;background:var(--bg)}
  body{position:relative;font-family:'Questrial',sans-serif;color:var(--ink)}
  .spread{position:absolute;left:62px;top:12px;width:1076px;height:816px;background:var(--paper);box-shadow:0 6px 24px rgba(0,0,0,.18);overflow:hidden}
  .abs{position:absolute}
  .gutter{position:absolute;left:537px;top:0;width:2px;height:816px;background:rgba(0,0,0,.06)}
  .tab{background:var(--orange);color:#fff;font-family:'PT Serif',serif;font-weight:400;text-transform:uppercase;display:flex;align-items:flex-end;justify-content:center}

  /* left page */
  .about-tab{left:31px;top:0;width:131px;height:70px;font-size:16px;padding-bottom:12px}
  .about-text{left:34px;top:80px;width:298px;font-size:10px;line-height:12.8px;text-align:justify}
  .values{left:330px;top:52px}
  .photo{background:linear-gradient(180deg,#6f9a5a 0%,#8fb86a 35%,#3f8fc8 60%,#5aa6dc 100%)}
  .photo-race{left:31px;top:228px;width:451px;height:312px}
  .top-three{left:0;top:540px;width:286px;height:84px;background:var(--slate);color:#fff;font-family:'PT Serif',serif;display:flex;align-items:center;padding-left:40px}
  .top-three .lead{font-size:12px;margin-top:14px}
  .top-three .num{font-size:32px;margin:0 6px}
  .top-three .heads{font-size:12px;line-height:16px;text-transform:uppercase}
  .top-three .note{font-family:'Questrial',sans-serif;font-size:8.5px;margin-top:6px;color:#e8e8e8}
  .quote{left:302px;top:548px;width:176px;color:var(--red);font-size:9px;line-height:12px;text-align:center;text-transform:uppercase}
  .quote .mark{font-family:'PT Serif',serif;font-weight:700;color:#333;font-size:44px;line-height:20px}
  .quote .open{position:absolute;left:2px;top:6px}
  .quote .close{font-size:30px;vertical-align:-14px;margin-left:4px}
  .love{left:38px;width:248px;display:flex;gap:14px;font-size:10.5px;line-height:14px;color:#444;text-align:justify}
  .love svg{flex:none;margin-top:4px}
  .love-1{top:630px}.love-2{top:678px}.love-3{top:736px}

  .team-title{left:296px;top:630px;width:464px;display:flex;align-items:center;gap:6px;font-family:'PT Serif',serif;color:var(--sky);font-size:27px}
  .team-title .rule{flex:1;height:1.5px;background:var(--sky)}
  .team{left:292px;top:674px;width:476px;display:flex;justify-content:space-between;list-style:none}
  .member{width:70px;text-align:center;font-family:'PT Serif',serif;font-size:6.8px;line-height:8.5px;color:#333;white-space:nowrap;display:flex;flex-direction:column;align-items:center}
  .member svg{display:block;margin:0 0 6px}

  /* middle */
  .way-title{left:524px;top:72px;width:240px;text-align:center;font-size:17px;line-height:21px;text-transform:uppercase}
  .way-text{left:553px;top:122px;width:211px;font-size:10.8px;line-height:13.6px;text-align:justify;color:#333}
  .p1{left:513px;top:238px;width:242px;height:134px;background:linear-gradient(180deg,#d9d2c4,#5b4a47 70%,#c23a34)}
  .p2{left:513px;top:378px;width:118px;height:117px;background:linear-gradient(160deg,#cfc6bb,#7c7068)}
  .p3{left:513px;top:501px;width:118px;height:104px;background:linear-gradient(160deg,#e4ddd3,#8d7d70)}
  .p4{left:637px;top:378px;width:118px;height:227px;background:linear-gradient(180deg,#d8d3cc,#a98360 75%,#8b5c36)}

  /* right page */
  .fix-tab{left:779px;top:0;width:264px;height:60px;font-size:19px;padding-bottom:6px}
  .step-head{left:795px;display:flex;align-items:flex-start;gap:14px}
  .step-head .n{font-size:27px;line-height:28px;color:#222;width:28px}
  .step-head h3{font-weight:400;font-size:11px;line-height:13px;margin-top:8px;text-transform:uppercase}
  .step-head .sub{font-family:'PT Serif',serif;font-size:6px;line-height:8px;display:block;color:#333;text-transform:none}
  .step-list{left:837px;width:212px;list-style:none}
  .step-list li{position:relative;font-family:'PT Serif',serif;font-size:10.2px;line-height:13px;margin-bottom:4px}
  .step-list li::before{content:"";position:absolute;left:-15px;top:3px;width:7px;height:7px;background:var(--teal);clip-path:polygon(50% 0,65% 35%,100% 50%,65% 65%,50% 100%,35% 65%,0 50%,35% 35%)}
  .c-red{color:var(--red)} .c-amber{color:var(--amber)} .c-green{color:var(--green)} .c-dark{color:var(--dark-green)}
  .biohack{left:745px;top:422px;width:193px;height:28px;background:var(--blue);border-radius:0 14px 14px 0;color:#fff;font-family:'PT Serif',serif;font-style:italic;font-size:10.5px;display:flex;align-items:center;padding-left:42px}
  .biohack-dot{left:735px;top:413px}
</style>
</head>
<body>
<div class="spread">
  <svg class="abs" style="left:460px;top:0" width="156" height="42" viewBox="0 0 156 42" aria-hidden="true">
    <polygon points="0,0 78,42 78,0" fill="var(--deep-orange)"/>
    <polygon points="78,0 78,42 156,0" fill="var(--orange)"/>
  </svg>
  <svg class="abs" style="left:460px;top:774px" width="156" height="42" viewBox="0 0 156 42" aria-hidden="true">
    <polygon points="0,42 78,0 78,42" fill="var(--deep-orange)"/>
    <polygon points="78,0 78,42 156,42" fill="var(--orange)"/>
  </svg>

  <!-- left page -->
  <h2 class="abs tab about-tab">About Us</h2>
  <p class="abs about-text">COURAGE gives us the strength and confidence to take risks and embrace challenges. INSPIRATION is our energy, our fuel for success, that life force that feeds us as we grow and develop. FUN generates happiness, and we all function at our best when we are happy. CREATIVITY sets us as an innovative leading-edge business. WOW means being the very best we can be and realise our true potential. We are not your average business, our service is not average, and our people are not average. TEAM and in particular high-performance team means we perform at our very best. Great teamwork creates unity and we accomplish much more than each of us alone.</p>
  <svg class="abs values" width="150" height="140" viewBox="330 60 150 140" font-family="PT Serif, serif" font-size="6.5" text-anchor="middle" fill="#333">
    <g fill="#fff" stroke="var(--deep-orange)" stroke-width="3">
      <circle cx="360" cy="91" r="23"/><circle cx="407" cy="93" r="23"/><circle cx="451" cy="95" r="23"/>
      <circle cx="384" cy="129" r="23"/><circle cx="428" cy="130" r="23"/><circle cx="407" cy="166" r="23"/>
    </g>
    <text x="360" y="93">COURAGE</text><text x="407" y="95" font-size="5.6">INSPIRATION</text><text x="451" y="97">FUN</text>
    <text x="384" y="131">CREATIVE</text><text x="428" y="132">WOW</text><text x="407" y="168">TEAM</text>
  </svg>
  <div class="abs photo photo-race" role="img" aria-label="Photo of seven masters sprinters in national singlets arm in arm on a blue athletics track"></div>

  <div class="abs top-three">
    <span class="lead">THE TOP</span><span class="num">3</span>
    <div><div class="heads">Things our clients<br>love about us</div><div class="note">(and hopefully yours will too!)</div></div>
  </div>
  <blockquote class="abs quote">
    <span class="mark open">“</span>
    <span style="padding-left:30px">At The Stride Studio, we are</span> passionate about building strong postural foundations, from the feet up.<span class="mark close">”</span>
  </blockquote>

  <div class="abs love love-1"><svg width="20" height="20" viewBox="0 0 20 20" aria-hidden="true"><g fill="var(--teal)"><rect x="7" y="0" width="6" height="6" transform="rotate(45 10 3)"/><rect x="7" y="14" width="6" height="6" transform="rotate(45 10 17)"/><rect x="0" y="7" width="6" height="6" transform="rotate(45 3 10)"/><rect x="14" y="7" width="6" height="6" transform="rotate(45 17 10)"/></g></svg><span>Positive energy, enthusiasm and outcomes NPS average score &gt;9 out of 10</span></div>
  <div class="abs love love-2"><svg width="20" height="20" viewBox="0 0 20 20" aria-hidden="true"><g fill="var(--teal)"><rect x="7" y="0" width="6" height="6" transform="rotate(45 10 3)"/><rect x="7" y="14" width="6" height="6" transform="rotate(45 10 17)"/><rect x="0" y="7" width="6" height="6" transform="rotate(45 3 10)"/><rect x="14" y="7" width="6" height="6" transform="rotate(45 17 10)"/></g></svg><span>Trusted leader in the practice of podiatric medicine established 1999, elite experience, latest high-tech equipment</span></div>
  <div class="abs love love-3"><svg width="20" height="20" viewBox="0 0 20 20" aria-hidden="true"><g fill="var(--teal)"><rect x="7" y="0" width="6" height="6" transform="rotate(45 10 3)"/><rect x="7" y="14" width="6" height="6" transform="rotate(45 10 17)"/><rect x="0" y="7" width="6" height="6" transform="rotate(45 3 10)"/><rect x="14" y="7" width="6" height="6" transform="rotate(45 17 10)"/></g></svg><span>Focus is on strong feet, not just orthotics! Groundwork Barefoot Training, Fascial Lines, Foot Manual Therapies</span></div>

  <!-- middle -->
  <h2 class="abs way-title" style="font-weight:400">The<br>Stride Studio Way</h2>
  <p class="abs way-text">Our pathway to strengthen postural foundations, to create lasting changes for freedom of movement, and ultimately keep us going well beyond what we thought was possible (updated as research and tech changes).</p>

  <div class="abs photo p1" role="img" aria-label="Group photo of the practice team and workshop attendees"></div>
  <div class="abs photo p2" role="img" aria-label="Photo of a presenter teaching a seminar"></div>
  <div class="abs photo p3" role="img" aria-label="Photo of two presenters speaking to an audience"></div>
  <div class="abs photo p4" role="img" aria-label="Photo of a movement workshop in a studio with a timber floor"></div>

  <!-- right page -->
  <h2 class="abs tab fix-tab">Fix Your Feet</h2>

  <div class="abs step-head" style="top:72px"><span class="n">01</span><h3 class="c-red">Fix the pain</h3></div>
  <ul class="abs step-list" style="top:102px"><li>Provide analgesia</li><li>Reduce inflammation</li><li>Corn/callus/foreign body removal</li><li>Ingrown/thickened toenail repair and maintenance</li><li>Surgery</li></ul>

  <div class="abs step-head" style="top:204px"><span class="n">02</span><h3 class="c-amber">Protect the feet<span class="sub">(reduce damage, optimise stability, promote healing)</span></h3></div>
  <ul class="abs step-list" style="top:245px"><li>Reduce tissue damage</li><li>Optimise Foot Posture</li><li>Activate neuromuscular/reflexive balance stability</li><li>Promote tissue repair/cellular regeneration</li></ul>

  <div class="abs step-head" style="top:328px"><span class="n">03</span><h3 class="c-green">Strengthen the feet<span class="sub">(increase strength and resilience)</span></h3></div>
  <ul class="abs step-list" style="top:369px"><li>Strengthen intrinsics</li><li>Connect foot strength to core strength</li><li>Stimulate neuromuscular strength</li></ul>

  <div class="abs biohack">Biohack your body</div>
  <svg class="abs biohack-dot" width="46" height="46" viewBox="0 0 46 46" aria-hidden="true">
    <circle cx="23" cy="23" r="22" fill="var(--blue)"/><circle cx="23" cy="23" r="15" fill="#fff"/><circle cx="23" cy="23" r="11" fill="none" stroke="#d6dbe2" stroke-width="3"/>
  </svg>

  <div class="abs step-head" style="top:450px"><span class="n">04</span><h3 class="c-green">Protect the whole body<span class="sub" style="padding-left:62px">(stability)</span></h3></div>
  <ul class="abs step-list" style="top:485px"><li>Optimise Postural Alignment</li><li>Activate neuromuscular/reflexive balance stability</li><li>Customised corrective exercises</li><li>Improve cellular regeneration</li><li>Optimise nutrition/healthy gut</li><li>Optimise healthy mind</li></ul>

  <div class="abs step-head" style="top:600px"><span class="n">05</span><h3 class="c-dark">Strengthen the whole body<span class="sub">(strength, elasticity)</span></h3></div>
  <ul class="abs step-list" style="top:638px;width:230px"><li>Strengthen the deep core (stabilisers)</li><li>Strengthen the outer core (mobilisers)</li><li>Increase fascial elasticity/strength</li><li>Increase functional strength</li><li>Increase endurance</li><li>Customised nutrition for specific performance</li><li>Improve psychological resilience</li></ul>

  <div class="abs step-head" style="top:762px"><span class="n">06</span><h3>Repeat consistently</h3></div>

  <div class="gutter"></div>

  <div class="abs team-title"><span class="rule"></span><span>OUR TEAM</span><span class="rule"></span></div>
  <ul class="abs team">
    <li class="member"><svg width="64" height="76" viewBox="0 0 66 78" role="img" aria-label="Portrait of the principal podiatrist"><polygon points="33,2 64,20 64,58 33,76 2,58 2,20" fill="#c9ccd1" stroke="#8fc9c4" stroke-width="4"/></svg>Dr Ravi Kandasamy<br>Principal Podiatrist</li>
    <li class="member"><svg width="64" height="76" viewBox="0 0 66 78" role="img" aria-label="Portrait of the senior podiatrist"><polygon points="33,2 64,20 64,58 33,76 2,58 2,20" fill="#c9a99c" stroke="var(--green)" stroke-width="4"/></svg>Dr Claire Hollis<br>Senior Podiatrist</li>
    <li class="member"><svg width="64" height="76" viewBox="0 0 66 78" role="img" aria-label="Portrait of a podiatrist"><polygon points="33,2 64,20 64,58 33,76 2,58 2,20" fill="#bfb7b2" stroke="#f1d318" stroke-width="4"/></svg>Dr Nadia Fenwick<br>Podiatrist</li>
    <li class="member"><svg width="64" height="76" viewBox="0 0 66 78" role="img" aria-label="Portrait of a podiatrist"><polygon points="33,2 64,20 64,58 33,76 2,58 2,20" fill="#c5c8ce" stroke="#2b4a8f" stroke-width="4"/></svg>Dr Marcus Teo<br>Podiatrist</li>
    <li class="member"><svg width="64" height="76" viewBox="0 0 66 78" role="img" aria-label="Portrait of the practice manager"><polygon points="33,2 64,20 64,58 33,76 2,58 2,20" fill="#c9c0b8" stroke="var(--red)" stroke-width="4"/></svg>Jenny Calder<br>Practice Manager</li>
    <li class="member"><svg width="64" height="76" viewBox="0 0 66 78" role="img" aria-label="Portrait of the front office administrator"><polygon points="33,2 64,20 64,58 33,76 2,58 2,20" fill="#b7aaa3" stroke="var(--sky)" stroke-width="4"/></svg>Tessa Marlow<br>Front Office Administrator</li>
  </ul>
</div>
</body>
</html>
```